Cobalt Bridge Capital - Letterhead

We need letterhead options for our case funding company called Cobalt Bridge Capital. Here are some of the details:

Name - Cobalt Bridge Capital
Phone - (555) 214 - 9087
Address - 58 Harlow Lane
Suite 312
New York, NY 10482
Website - cobaltbridgecapital.example

```html
<!DOCTYPE html>
<html lang="en">
<head>
<meta charset="utf-8">
<title>Cobalt Bridge Capital – Letterhead</title>
<link href="https://fonts.googleapis.com/css2?family=Questrial&family=Roboto:wght@400&display=swap" rel="stylesheet">
<style>
  :root {
    --backdrop: #e6e6e6;
    --paper: #f1f1f1;
    --navy: #1c3a55;
    --slate: #8a99a6;
    --ink: #4a4a4a;
    --ink-soft: #5c5c5c;
    --rule: #2b2b2b;
    --divider: #4d6f95;
    --signature: #3f6fb5;
  }
  * { box-sizing: border-box; margin: 0; padding: 0; }
  html, body {
    width: 1024px; height: 1200px; overflow: hidden;
    background: var(--backdrop);
  }
  .letterhead {
    position: absolute; left: 106px; top: 26px;
    width: 812px; height: 1148px;
    background: var(--paper);
    font-family: "Questrial", sans-serif;
    color: var(--ink);
  }
  .brand {
    position: absolute; top: 92px; left: 0; width: 100%;
    display: flex; justify-content: center; align-items: center; gap: 16px;
  }
  .brand-dot {
    width: 64px; height: 64px; border-radius: 50%;
    background: var(--navy);
  }
  .brand-name {
    font-family: "Questrial", sans-serif;
    color: var(--navy);
    font-size: 21px; line-height: 24px; letter-spacing: 2.5px;
    text-transform: uppercase;
  }
  .salutation {
    position: absolute; left: 75px; top: 334px;
    font-size: 19px; color: var(--ink-soft);
  }
  .body-copy {
    position: absolute; left: 75px; right: 70px; top: 384px;
    font-size: 11.6px; line-height: 15.5px; color: var(--ink-soft);
    text-align: justify;
  }
  .body-copy p + p { margin-top: 15px; }
  .closing {
    position: absolute; left: 75px; top: 732px;
    font-size: 11.6px; color: var(--ink-soft);
  }
  .signature {
    position: absolute; left: 72px; top: 786px;
    width: 150px; height: 56px; border-radius: 4px;
    background: linear-gradient(90deg, rgba(63,111,181,0.18), rgba(63,111,181,0.08));
  }
  .footer-rule {
    position: absolute; left: 75px; right: 70px; top: 997px;
    border-top: 1px solid var(--rule);
  }
  .footer {
    position: absolute; left: 75px; right: 70px; top: 1020px;
    display: flex; justify-content: space-between; align-items: flex-start;
    font-family: "Roboto", sans-serif; font-size: 11.2px; line-height: 14px;
    color: var(--ink); text-transform: uppercase;
  }
  .contact { display: flex; gap: 8px; align-items: flex-start; }
  .contact svg { flex: none; width: 18px; height: 18px; margin-top: -2px; }
  .divider { width: 1px; height: 44px; background: var(--divider); }
  .contact-web { text-transform: uppercase; }
</style>
</head>
<body>
  <main class="letterhead">
    <header class="brand">
      <div class="brand-dot"></div>
      <div class="brand-name">Cobalt<br>Bridge<br>Capital</div>
    </header>

    <p class="salutation">Dear Mr. Avery,</p>

    <section class="body-copy">
      <p>Lorem ipsum dolor sit amet, consectetur adipiscing elit. Donec orci purus, luctus vitae dignissim eu, iaculis sed purus. Vivamus faucibus, ipsum nec aliquet viverra, leo mauris condimentum ligula, sit amet sagittis enim ligula quis arcu. Nam egestas tortor id nisi porttitor mattis. In tortor ante, ultricies in suscipit a, tempus non massa. Vivamus et auctor mi. Fusce vel massa nulla. Phasellus nec eros mauris, et scelerisque orci.</p>
      <p>Donec malesuada orci vitae nulla accumsan porta a id massa. Quisque accumsan iaculis magna sit amet fringilla. Maecenas consequat, magna eget tincidunt semper, odio nibh rutrum mi, id feugiat ante nisi eu risus. Vestibulum nunc orci, rhoncus a placerat in, ultricies in mi. Cras mattis varius eros, vel fringilla nisi suscipit eget. Quisque scelerisque sagittis nulla at porttitor.</p>
      <p>Sed id augue vitae urna euismod commodo aliquet a quam. Pellentesque arcu velit, cursus et malesuada ut, consequat et diam. Nullam erat sem, rhoncus id ullamcorper vitae, rhoncus et arcu. In ultricies ultricies nulla, ut rutrum nisi iaculis at. Donec eu magna a metus ornare faucibus. Fusce aliquet faucibus ultricies. Morbi semper, est id tincidunt gravida, sem arcu adipiscing lacus, ac bibendum nulla leo eu purus. Quisque nec diam sed risus consectetur accumsan quis quis nibh. Vestibulum id purus lorem.</p>
      <p>It is a long established fact that a reader will be distracted by the readable content of a page when looking at its layout. The point of using Lorem Ipsum is that it has a more-or-less normal distribution of letters, as opposed to using 'Content here, content here', making it look like readable English. Many desktop publishing packages</p>
    </section>

    <p class="closing">Sincerely,</p>
    <div class="signature" role="img" aria-label="Handwritten signature of Daniel Avery in blue ink"></div>

    <div class="footer-rule"></div>
    <footer class="footer">
      <div class="contact">
        <svg viewBox="0 0 18 18" aria-hidden="true">
          <circle cx="9" cy="9" r="9" fill="var(--navy)"/>
          <path d="M9 4.2a3 3 0 0 0-3 3c0 2.3 3 6 3 6s3-3.7 3-6a3 3 0 0 0-3-3zm0 4.2a1.2 1.2 0 1 1 0-2.4 1.2 1.2 0 0 1 0 2.4z" fill="#fff"/>
        </svg>
        <address style="font-style:normal">58 Harlow Lane<br>Suite 312,<br>New York, NY 10482</address>
      </div>
      <div class="divider"></div>
      <div class="contact">
        <svg viewBox="0 0 18 18" aria-hidden="true">
          <circle cx="9" cy="9" r="9" fill="var(--navy)"/>
          <path d="M6.3 4.6l1.3 1.9-.8 1c.5 1.2 1.3 2 2.5 2.6l1-.8 1.9 1.3-.6 1.5c-3.3-.3-6.4-3.4-6.8-6.8z" fill="#fff"/>
        </svg>
        <span>(555) 214 - 9087</span>
      </div>
      <div class="divider"></div>
      <div class="contact">
        <svg viewBox="0 0 18 18" aria-hidden="true">
          <circle cx="9" cy="9" r="9" fill="var(--navy)"/>
          <circle cx="9" cy="9" r="4.3" fill="none" stroke="#fff" stroke-width="1.2"/>
          <path d="M4.7 9h8.6M9 4.7c1.6 1.6 1.6 7 0 8.6M9 4.7c-1.6 1.6-1.6 7 0 8.6" fill="none" stroke="#fff" stroke-width="0.9"/>
        </svg>
        <span class="contact-web">cobaltbridgecapital.example</span>
      </div>
    </footer>
  </main>
</body>
</html>
```